A website for Varnholt Limited

We need a new and modern website for our company. We are engineering consultants and contractors (EPC) in the oil and gas industry and building services industry.
What we do:
Engineering, procurement, construction
Automation (safety and process)
Non-destructive testing
Training
We have an existing website and the content can be referred from there since we are remaking the website
For more information visit Varnholt Limited Kenya

Coding

Number of Pages Required

1 page

```html
<!DOCTYPE html>
<html lang="en">
<head>
<meta charset="utf-8">
<title>Varnholt Limited — Engineering Consultants and Contractors</title>
<link rel="stylesheet" href="https://fonts.googleapis.com/css2?family=Roboto+Slab:wght@400;600;700;800&family=PT+Serif:ital,wght@0,400;0,700;1,400&display=swap">
<style>
:root{
  --blue:#0b4fa3;
  --blue-deep:#0a3d7e;
  --blue-dark:#082c5c;
  --ink:#1b1b1b;
  --text:#444;
  --grey-bg:#f0f0f0;
  --dark-bg:#4a4a4a;
  --white:#fff;
  --footer-bar:#6b6b6b;
}
*{box-sizing:border-box;margin:0;padding:0}
html,body{width:1200px;height:4724px;overflow:hidden}
body{font-family:"PT Serif",Georgia,serif;color:var(--text);background:var(--white)}
h1,h2,h3,h4,.brand,.nav,.btn{font-family:"Roboto Slab",Georgia,serif}
section,header,footer{position:relative;width:1200px}

/* Hero */
.hero{height:648px;overflow:hidden}
.hero-photo{position:absolute;inset:0;background:linear-gradient(160deg,#6d7f8e 0%,#8a8a80 35%,#b4924f 60%,#5a6470 100%)}
.hero-shade{position:absolute;inset:0;background:rgba(10,25,45,.45)}
.topbar{position:absolute;top:0;left:0;right:0;height:112px;display:flex;align-items:center;padding:0 40px;background:rgba(0,0,0,.35)}
.brand{display:flex;align-items:center;gap:12px;color:var(--white);font-weight:800;font-size:26px;line-height:1}
.brand-mark{width:40px;height:40px;background:var(--blue)}
.nav{display:flex;gap:34px;margin-left:120px;font-size:16px;color:var(--white)}
.nav a{color:inherit;text-decoration:none}
.nav a.active{border-bottom:2px solid var(--white);padding-bottom:4px}
.phone{margin-left:auto;display:flex;align-items:center;gap:12px;color:var(--white);font-size:16px}
.phone-icon{width:32px;height:32px;border-radius:50%;background:var(--blue);display:flex;align-items:center;justify-content:center}
.hero-copy{position:absolute;top:285px;left:0;right:0;text-align:center;color:var(--white)}
.hero-copy h1{font-size:44px;font-weight:700;letter-spacing:1px}
.hero-copy p{font-family:"Roboto Slab",serif;font-size:22px;font-weight:600;margin-top:6px}
.btn{display:inline-block;background:var(--blue);color:var(--white);font-size:15px;font-weight:600;padding:12px 26px;border:none}
.hero-copy .btn{margin-top:22px}
.arrow{position:absolute;top:344px;width:30px;height:30px}
.arrow.left{left:34px}.arrow.right{right:34px}

/* Heading */
.section-title{font-size:44px;font-weight:700;color:var(--ink);text-align:center}
.section-title::after{content:"";display:block;width:90px;height:5px;background:var(--blue);margin:12px auto 0}

/* Who we are */
.who{height:704px}
.who-block{position:absolute;left:88px;top:212px;width:344px;height:380px;background:var(--blue)}
.who-photo{position:absolute;left:148px;top:152px;width:392px;height:392px;background:linear-gradient(135deg,#c9cdd2,#d39a3c 55%,#6b7b8c);box-shadow:0 8px 24px rgba(0,0,0,.25)}
.who-copy{position:absolute;left:592px;top:170px;width:500px}
.who-copy h2{font-size:44px;font-weight:700;color:var(--ink);letter-spacing:1px}
.who-copy h2::after{content:"";display:block;width:110px;height:5px;background:var(--blue);margin-top:8px}
.who-copy p{font-size:17px;line-height:1.5;margin-top:26px}
.who-copy p.lead{font-size:20px;font-weight:700;color:var(--ink);margin-top:22px;line-height:1.45}

/* Services */
.services{height:900px;background:var(--grey-bg)}
.services .section-title{padding-top:90px}
.service-grid{position:absolute;left:148px;top:196px;display:grid;grid-template-columns:repeat(3,282px);column-gap:26px;row-gap:36px}
.card{height:256px;background:var(--white);box-shadow:0 3px 12px rgba(0,0,0,.12);text-align:center;padding-top:26px;position:relative}
.card::after{content:"";position:absolute;left:65px;right:65px;bottom:0;height:6px;background:var(--blue)}
.hex{width:92px;height:100px;margin:0 auto}
.card h3{font-size:20px;font-weight:700;color:var(--blue-deep);margin-top:14px}
.card p{font-size:13px;line-height:1.4;margin:10px 34px 0}

/* Works */
.works{height:820px;background:var(--dark-bg);overflow:hidden}
.works-bg{position:absolute;inset:0;background:linear-gradient(120deg,#3c3c3c,#5c5c5c 50%,#404040)}
.works .section-title{position:relative;color:var(--white);padding-top:76px}
.work-grid{position:absolute;left:152px;top:196px;width:896px;display:grid;grid-template-columns:repeat(3,1fr);grid-template-rows:224px 224px;gap:12px}
.work{position:relative}
.work.wide{grid-column:span 2;background:linear-gradient(160deg,#7fa3c4,#2f5f8f 60%,#1f3f66)}
.work .zoom{position:absolute;left:50%;top:50%;transform:translate(-50%,-50%)}
.w2{background:linear-gradient(150deg,#d8dde2,#9a9080 60%,#6c7480)}
.w3{background:linear-gradient(150deg,#c7c0b2,#8b8072 60%,#5c5a55)}
.w4{background:linear-gradient(150deg,#e7b070,#5a6d86 60%,#34465e)}
.w5{background:linear-gradient(150deg,#c9d3dc,#d49a3e 55%,#4f5d6c)}
.works .btn{position:absolute;left:516px;top:2720px}
.works .view-all{position:absolute;left:50%;transform:translateX(-50%);top:700px}

/* Testimonials */
.testimonials{height:708px;text-align:center}
.testimonials .section-title{padding-top:100px}
.quote{font-style:italic;font-size:17px;line-height:1.55;width:760px;margin:28px auto 0;color:var(--text)}
.person{display:flex;align-items:center;justify-content:center;gap:16px;margin-top:18px}
.avatar{width:96px;height:96px;border-radius:50%;background:linear-gradient(135deg,#8ec06a,#c99b6a)}
.person-name{text-align:left}
.person-name h4{font-size:17px;font-weight:600;color:var(--ink)}
.person-name span{font-size:12px}
.partners{display:flex;justify-content:center;gap:96px;margin-top:48px;align-items:center}
.partner{width:70px;height:70px;background:#2a2a2a;border-radius:50%}
.partner.sq{border-radius:0;width:64px;height:64px}

/* Contact */
.contact{height:520px;overflow:hidden}
.contact-bg{position:absolute;inset:0;background:linear-gradient(120deg,var(--blue-dark),var(--blue) 55%,#1766c4)}
.contact-copy{position:absolute;left:152px;top:160px;width:420px;color:var(--white)}
.contact-copy h2{font-size:30px;font-weight:700}
.contact-copy h2::after{content:"";display:block;width:60px;height:4px;background:var(--white);margin-top:6px}
.contact-copy p{font-size:15px;line-height:1.45;margin-top:16px}
.contact-line{display:flex;align-items:center;gap:12px;font-family:"Roboto Slab",serif;font-size:20px;font-weight:600;margin-top:20px}
.contact-form{position:absolute;left:660px;top:92px;width:372px;height:328px;background:rgba(10,40,90,.55);padding:16px}
.field{height:38px;border:1px solid rgba(255,255,255,.8);border-radius:4px;color:var(--white);font-size:13px;padding:10px 12px;margin-bottom:14px}
.field.msg{height:96px}
.contact-form .btn{display:block;margin:12px auto 0;border-radius:20px;padding:10px 24px;font-size:14px;background:#1a1a2e;width:max-content}

/* Footer */
.site-footer{height:424px}
.footer-cols{position:absolute;left:152px;top:108px;display:grid;grid-template-columns:344px 180px 200px 180px;gap:0}
.footer-cols h4{font-size:15px;font-weight:700;color:var(--ink)}
.footer-cols h4::after{content:"";display:block;width:40px;height:3px;background:var(--blue);margin-top:5px}
.footer-cols p,.footer-cols li{font-size:13px;line-height:1.5;color:var(--text);list-style:none}
.footer-cols p{margin-top:22px;width:250px}
.footer-cols ul{margin-top:18px}
.social{display:flex;gap:10px;margin-top:12px}
.social span{width:20px;height:20px;background:var(--blue)}
.copyright{position:absolute;left:0;right:0;bottom:0;height:72px;background:var(--footer-bar);color:var(--white);font-size:13px;display:flex;align-items:center;justify-content:center}
</style>
</head>
<body>

<header class="hero">
  <div class="hero-photo" role="img" aria-label="Engineers in hard hats and safety vests reviewing plans at a construction site"></div>
  <div class="hero-shade"></div>
  <div class="topbar">
    <div class="brand"><span class="brand-mark"></span>VARNHOLT LIMITED</div>
    <nav class="nav">
      <a class="active" href="#">Home</a><a href="#">About Us</a><a href="#">What we do</a><a href="#">Team</a><a href="#">Projects</a><a href="#">Contact</a>
    </nav>
    <div class="phone">
      <span class="phone-icon"><svg width="16" height="16" viewBox="0 0 24 24"><path fill="#fff" d="M6.6 10.8a15 15 0 0 0 6.6 6.6l2.2-2.2c.3-.3.7-.4 1-.2 1.1.4 2.3.6 3.6.6.6 0 1 .4 1 1V20c0 .6-.4 1-1 1A17 17 0 0 1 3 4c0-.6.4-1 1-1h3.5c.6 0 1 .4 1 1 0 1.3.2 2.5.6 3.6.1.3 0 .7-.2 1z"/></svg></span>
      (555) 345 0192
    </div>
  </div>
  <div class="hero-copy">
    <h1>VARNHOLT LIMITED</h1>
    <p>We are engineering consultants and contractors</p>
    <a class="btn" href="#">LEARN MORE</a>
  </div>
  <svg class="arrow left" viewBox="0 0 24 24"><path d="M15 5l-7 7 7 7" fill="none" stroke="#fff" stroke-width="3"/></svg>
  <svg class="arrow right" viewBox="0 0 24 24"><path d="M9 5l7 7-7 7" fill="none" stroke="#fff" stroke-width="3"/></svg>
</header>

<section class="who">
  <div class="who-block"></div>
  <div class="who-photo" role="img" aria-label="Engineers in hard hats studying blueprints on site"></div>
  <div class="who-copy">
    <h2>WHO WE ARE</h2>
    <p>Lorem ipsum dolor sit amet, consectetur adipiscing elit, sed do eiusmod tempor incididunt ut labore et dolore magna aliqua. Quis ipsum suspendisse ultrices gravida. Risus commodo viverra maecenas accumsan lacus vel facilisis.</p>
    <p class="lead">We are engineering consultants and contractors (EPC) in the oil and gas industry and building services industry.</p>
  </div>
</section>

<section class="services">
  <h2 class="section-title">WHAT WE DO</h2>
  <div class="service-grid">
    <article class="card">
      <svg class="hex" viewBox="0 0 92 100"><polygon points="46,2 90,27 90,73 46,98 2,73 2,27" fill="var(--blue)"/><circle cx="46" cy="50" r="16" fill="none" stroke="#fff" stroke-width="4"/><circle cx="46" cy="50" r="5" fill="#fff"/></svg>
      <h3>Engineering</h3>
      <p>Lorem ipsum dolor sit amet, cons adipiscing elit, sed do eiusmod te incididunt ut labore et dolore</p>
    </article>
    <article class="card">
      <svg class="hex" viewBox="0 0 92 100"><polygon points="46,2 90,27 90,73 46,98 2,73 2,27" fill="var(--blue)"/><rect x="32" y="32" width="28" height="36" fill="none" stroke="#fff" stroke-width="4"/><path d="M38 44h16M38 52h16M38 60h10" stroke="#fff" stroke-width="3"/></svg>
      <h3>Procurement</h3>
      <p>Lorem ipsum dolor sit amet, cons adipiscing elit, sed do eiusmod te incididunt ut labore et dolore</p>
    </article>
    <article class="card">
      <svg class="hex" viewBox="0 0 92 100"><polygon points="46,2 90,27 90,73 46,98 2,73 2,27" fill="var(--blue)"/><path d="M28 54a18 18 0 0 1 36 0z" fill="#fff"/><rect x="26" y="56" width="40" height="5" fill="#fff"/></svg>
      <h3>Construction</h3>
      <p>Lorem ipsum dolor sit amet, cons adipiscing elit, sed do eiusmod te incididunt ut labore et dolore</p>
    </article>
    <article class="card">
      <svg class="hex" viewBox="0 0 92 100"><polygon points="46,2 90,27 90,73 46,98 2,73 2,27" fill="var(--blue)"/><path d="M30 68h32M36 68V56l12-16 10 8" fill="none" stroke="#fff" stroke-width="4"/><circle cx="58" cy="50" r="4" fill="#fff"/></svg>
      <h3>Automation</h3>
      <p>Lorem ipsum dolor sit amet, cons adipiscing elit, sed do eiusmod te incididunt ut labore et dolore</p>
    </article>
    <article class="card">
      <svg class="hex" viewBox="0 0 92 100"><polygon points="46,2 90,27 90,73 46,98 2,73 2,27" fill="var(--blue)"/><rect x="28" y="34" width="30" height="30" fill="none" stroke="#fff" stroke-width="4"/><path d="M34 56l6-8 5 5 7-10" fill="none" stroke="#fff" stroke-width="3"/><path d="M56 62l8 8" stroke="#fff" stroke-width="5"/></svg>
      <h3>Non-destructive testing</h3>
      <p>Lorem ipsum dolor sit amet, cons adipiscing elit, sed do eiusmod te incididunt ut labore et dolore</p>
    </article>
    <article class="card">
      <svg class="hex" viewBox="0 0 92 100"><polygon points="46,2 90,27 90,73 46,98 2,73 2,27" fill="var(--blue)"/><rect x="26" y="32" width="40" height="26" fill="none" stroke="#fff" stroke-width="4"/><path d="M46 58v12M36 70h20" stroke="#fff" stroke-width="4"/></svg>
      <h3>Training</h3>
      <p>Lorem ipsum dolor sit amet, cons adipiscing elit, sed do eiusmod te incididunt ut labore et dolore</p>
    </article>
  </div>
</section>

<section class="works">
  <div class="works-bg" role="img" aria-label="Dimmed photo of engineers at work on a project"></div>
  <h2 class="section-title">OUR WORKS</h2>
  <div class="work-grid">
    <div class="work wide" role="img" aria-label="Oil and gas processing plant under a blue sky">
      <svg class="zoom" width="56" height="56" viewBox="0 0 56 56"><circle cx="24" cy="24" r="16" fill="none" stroke="#fff" stroke-width="4"/><path d="M36 36l14 14M24 16v16M16 24h16" stroke="#fff" stroke-width="4"/></svg>
    </div>
    <div class="work w2" role="img" aria-label="Two engineers in hard hats on site"></div>
    <div class="work w3" role="img" aria-label="Team reviewing drawings at a desk"></div>
    <div class="work w4" role="img" aria-label="Engineers at a construction site at sunset"></div>
    <div class="work w5" role="img" aria-label="Engineer holding plans in front of a structure"></div>
  </div>
  <a class="btn view-all" href="#">VIEW ALL</a>
</section>

<section class="testimonials">
  <h2 class="section-title">TESTIMONIALS</h2>
  <p class="quote">Lorem ipsum dolor sit amet, consectetur adipiscing elit, sed do eiusmod tempor incididunt ut labore et dolore magna aliqua. Quis ipsum suspendisse ultrices gravida. Risus commodo viverra maecenas accumsan lacus vel facilisis.</p>
  <div class="person">
    <div class="avatar" role="img" aria-label="Portrait of the client"></div>
    <div class="person-name"><h4>DORIN KALVIK</h4><span>Lorem Ipsum</span></div>
  </div>
  <div class="partners">
    <span class="partner"></span><span class="partner sq"></span><span class="partner"></span><span class="partner sq"></span><span class="partner"></span>
  </div>
</section>

<section class="contact">
  <div class="contact-bg" role="img" aria-label="Blue-tinted photo of an engineering site"></div>
  <div class="contact-copy">
    <h2>CONTACT US</h2>
    <p>Lorem ipsum dolor sit amet, consectetur adipiscing elit, sed do eiusmod tempor incididunt ut labore et dolore magna aliqua. Quis ipsum suspendisse ultrices gravida.</p>
    <div class="contact-line"><svg width="20" height="16" viewBox="0 0 20 16"><rect width="20" height="16" fill="#fff"/><path d="M0 0l10 8 10-8" fill="none" stroke="var(--blue)" stroke-width="2"/></svg>hello@varnholt-mail.com</div>
    <div class="contact-line"><svg width="18" height="18" viewBox="0 0 24 24"><path fill="#fff" d="M6.6 10.8a15 15 0 0 0 6.6 6.6l2.2-2.2c.3-.3.7-.4 1-.2 1.1.4 2.3.6 3.6.6.6 0 1 .4 1 1V20c0 .6-.4 1-1 1A17 17 0 0 1 3 4c0-.6.4-1 1-1h3.5c.6 0 1 .4 1 1 0 1.3.2 2.5.6 3.6.1.3 0 .7-.2 1z"/></svg>+0405 551 209</div>
  </div>
  <form class="contact-form">
    <div class="field">Name</div>
    <div class="field">Email</div>
    <div class="field">Phone</div>
    <div class="field msg">Message</div>
    <span class="btn">SUBMIT NOW</span>
  </form>
</section>

<footer class="site-footer">
  <div class="footer-cols">
    <div><h4>ABOUT US</h4><p>Lorem ipsum dolor sit amet, consectetur adipiscing elit, sed do eiusmod tempor ut labore et dolore magna aliqua. Quis ipsum suspendisse ultrices.</p></div>
    <div><h4>QUICK LINKS</h4><ul><li>Home</li><li>About Us</li><li>Services</li><li>Team</li><li>Contact</li></ul></div>
    <div><h4>SUPPORT</h4><ul><li>Support</li><li>Help</li><li>Privacy Policy</li><li>Terms and Conditions</li></ul></div>
    <div><h4>CONNECT ME</h4><p style="width:170px;margin-top:18px">Lorem ipsum dolor sit amet, sed tempor adipiscing.</p><div class="social"><span></span><span></span><span></span></div></div>
  </div>
  <div class="copyright">Copyright © 2019 Varnholt Limited. All Rights Reserved</div>
</footer>

</body>
</html>
```